Business Card Design

We need a business card design that can also be aplied for postcards. We are a small indie record company that also do consulting, and development of independat artitst . I already have the name and the basic idea of what i am looking for but i am open to any suggestion.
Info for the card
Name of the company : Velmora Records
NAME : Tomas Invaldi
PHONE : 208-5536142
EMAIL : hello@velmorarecords.example
WEB: www.velmorarecords.example
Target Market(s)
Male - Female independent musicians ages 18 to 45
Industry/Entity Type
Record Company
Contact Information for Business Card
Independant records company that also works in consulting for music business models for independent artists
Look and feel
Each slider illustrates characteristics of the customer's brand and the style your logo design should communicate.

```html
<!DOCTYPE html>
<html lang="en">
<head>
<meta charset="utf-8">
<title>Velmora Records – Business Card</title>
<link rel="stylesheet" href="https://fonts.googleapis.com/css2?family=Open+Sans:wght@400;600&display=swap">
<style>
  :root {
    --card-bg: #ffffff;
    --ink: #0a0a0a;
    --panel-edge: #0f58a8;
    --panel-mid: #0a72b8;
    --panel-glow: #6fb3e0;
    --brand-text: #ffffff;
  }
  * { margin: 0; padding: 0; box-sizing: border-box; }
  html, body {
    width: 1200px;
    height: 702px;
    overflow: hidden;
    background: var(--card-bg);
  }
  .card {
    position: relative;
    width: 1200px;
    height: 702px;
    background: var(--card-bg);
    font-family: "Open Sans", Verdana, sans-serif;
    color: var(--ink);
  }
  .contact-list {
    position: absolute;
    left: 66px;
    top: 0;
    width: 530px;
    height: 702px;
  }
  .contact-row {
    position: absolute;
    left: 0;
    display: flex;
    align-items: center;
  }
  .contact-icon {
    width: 66px;
    height: 66px;
    flex: none;
  }
  .contact-text {
    margin-left: 46px;
    font-size: 26px;
    letter-spacing: 0;
    white-space: nowrap;
  }
  .contact-row.phone { top: 147px; }
  .contact-row.email { top: 334px; }
  .contact-row.web   { top: 525px; }

  .brand-panel {
    position: absolute;
    left: 612px;
    top: 22px;
    width: 588px;
    height: 664px;
    background: radial-gradient(circle at 32% 46%, var(--panel-glow) 0%, var(--panel-mid) 38%, var(--panel-edge) 72%);
  }
  .artwork-area {
    position: absolute;
    left: 90px;
    top: 300px;
    width: 420px;
    height: 300px;
  }
  .brand-name {
    position: absolute;
    left: 0;
    right: 0;
    top: 270px;
    display: flex;
    align-items: center;
    justify-content: center;
    gap: 16px;
    font-size: 46px;
    font-weight: 600;
    color: var(--brand-text);
    white-space: nowrap;
  }
  .brand-dot {
    width: 24px;
    height: 24px;
    border-radius: 50%;
    background: var(--brand-text);
  }
</style>
</head>
<body>
<main class="card">
  <div class="contact-list">
    <div class="contact-row phone">
      <svg class="contact-icon" viewBox="0 0 76 76" aria-hidden="true">
        <path fill="#0a0a0a" d="M20 4c3-2 6-1 7 2l6 13c1 3 0 5-2 6l-5 3c3 10 9 19 17 25l5-3c2-1 5-1 6 1l9 11c2 2 1 5-1 7l-5 4c-4 3-10 2-15-2C26 61 14 43 10 24 9 17 11 11 15 8z"/>
      </svg>
      <span class="contact-text">208-5536142</span>
    </div>

    <div class="contact-row email">
      <svg class="contact-icon" viewBox="0 0 76 76" aria-hidden="true">
        <rect x="0" y="11" width="76" height="54" fill="#0a0a0a"/>
        <path d="M1 12 L38 44 L75 12 M1 64 L28 36 M75 64 L48 36" fill="none" stroke="#ffffff" stroke-width="2"/>
      </svg>
      <span class="contact-text">hello@velmorarecords.example</span>
    </div>

    <div class="contact-row web">
      <svg class="contact-icon" viewBox="0 0 76 76" aria-hidden="true">
        <circle cx="38" cy="38" r="36" fill="#0a0a0a"/>
        <g fill="none" stroke="#ffffff" stroke-width="3">
          <ellipse cx="38" cy="38" rx="15" ry="36"/>
          <line x1="38" y1="2" x2="38" y2="74"/>
          <line x1="2" y1="38" x2="74" y2="38"/>
          <line x1="8" y1="20" x2="68" y2="20"/>
          <line x1="8" y1="56" x2="68" y2="56"/>
        </g>
      </svg>
      <span class="contact-text">www.velmorarecords.example</span>
    </div>
  </div>

  <section class="brand-panel">
    <div class="artwork-area" role="img" aria-label="Illustration of a tilted cassette tape"></div>
    <div class="brand-name">
      <span class="brand-dot" aria-hidden="true"></span>
      <span>Velmora Records</span>
    </div>
  </section>
</main>
</body>
</html>
```